Business Card for Voltrix

Horizontal business card for voltrix, the electrical contractor.
clean and professional looking, using company branding and colours.
I also want the blue in the logo and wording to be made a more 'electric' blue and the grey 'Voltrix' to be slightly darker.

Pleas use the following contact details:

Colin Marsh
Owner

t: 01736 582910
m: 07831 206719
e: colin@voltrix-installs.co.uk

www.voltrix-installs.co.uk

Industry/Entity Type

Electrical

Font styles to use
Sans Serif

```html
<!DOCTYPE html>
<html lang="en">
<head>
<meta charset="utf-8">
<title>Voltrix – Business Card</title>
<link rel="stylesheet" href="https://fonts.googleapis.com/css2?family=Arimo:wght@400;700&display=swap">
<style>
  :root {
    --backdrop: #d9dddd;
    --card: #ffffff;
    --electric-blue: #35d9f2;
    --soft-blue: #b9eef6;
    --brand-grey: #5c7171;
    --label-grey: #8a9696;
    --ink-white: #ffffff;
    --shadow: rgba(0, 0, 0, 0.28);
  }
  * { box-sizing: border-box; margin: 0; padding: 0; }
  html, body {
    width: 1200px;
    height: 750px;
    overflow: hidden;
    background: var(--backdrop);
    font-family: "Arimo", Arial, sans-serif;
  }
  .stage {
    width: 1200px;
    height: 750px;
    display: flex;
    align-items: center;
    justify-content: center;
    gap: 40px;
  }
  .card {
    position: relative;
    width: 540px;
    height: 298px;
    background: var(--card);
    box-shadow: 4px 5px 10px var(--shadow);
    overflow: hidden;
  }

  /* Front */
  .card-front__decor {
    position: absolute;
    left: 0;
    top: 0;
    width: 190px;
    height: 100%;
    background: linear-gradient(160deg, var(--soft-blue) 0%, #e6f8fb 45%, #e4e7e7 75%, #cfd4d4 100%);
    opacity: 0.85;
  }
  .card-front__decor--corner {
    left: auto;
    right: 0;
    top: auto;
    bottom: 0;
    width: 200px;
    height: 24px;
    background: linear-gradient(90deg, #e3f8fb 0%, var(--soft-blue) 60%, #cfd4d4 100%);
  }
  .brand {
    position: absolute;
    right: 130px;
    top: 80px;
    display: flex;
    flex-direction: column;
    align-items: flex-end;
  }
  .brand__dot {
    width: 30px;
    height: 30px;
    border-radius: 50%;
    background: var(--electric-blue);
    margin-right: 8px;
    margin-bottom: 28px;
  }
  .brand__name {
    font-size: 25px;
    font-weight: 400;
    letter-spacing: 0.28em;
    color: var(--brand-grey);
    text-transform: uppercase;
    line-height: 1;
    margin-right: -0.28em;
  }
  .brand__tagline {
    margin-top: 6px;
    font-size: 8.5px;
    letter-spacing: 0.06em;
    color: var(--electric-blue);
    text-transform: uppercase;
  }

  /* Back */
  .card-back__band {
    position: absolute;
    left: 0;
    right: 0;
    bottom: 0;
    height: 170px;
    background: var(--electric-blue);
  }
  .contact-name {
    position: absolute;
    right: 30px;
    top: 34px;
    text-align: right;
  }
  .contact-name__full {
    font-size: 19px;
    letter-spacing: 0.04em;
    color: var(--electric-blue);
    text-transform: uppercase;
  }
  .contact-name__role {
    margin-top: 4px;
    font-size: 7px;
    letter-spacing: 0.06em;
    color: var(--label-grey);
    text-transform: uppercase;
  }
  .contact-details {
    position: absolute;
    right: 30px;
    bottom: 26px;
    list-style: none;
    text-align: right;
    color: var(--ink-white);
    font-size: 11px;
    line-height: 1.55;
    letter-spacing: 0.02em;
  }
  .contact-details__phone { word-spacing: 0.35em; }
</style>
</head>
<body>
<main class="stage">
  <section class="card card-front" aria-label="Card front">
    <div class="card-front__decor" role="img" aria-label="Abstract flowing brand swirls in electric blue, pale blue, grey and black"></div>
    <div class="card-front__decor card-front__decor--corner" role="img" aria-label="Brand swirl edge in blue and black"></div>
    <div class="brand">
      <span class="brand__dot" aria-hidden="true"></span>
      <h1 class="brand__name">Voltrix</h1>
      <p class="brand__tagline">The Electrical Contractor</p>
    </div>
  </section>

  <section class="card card-back" aria-label="Card back">
    <div class="contact-name">
      <h2 class="contact-name__full">Colin Marsh</h2>
      <p class="contact-name__role">Owner</p>
    </div>
    <div class="card-back__band"></div>
    <ul class="contact-details">
      <li class="contact-details__phone">07831 206719</li>
      <li class="contact-details__phone">01736 582910</li>
      <li>colin@voltrix-installs.co.uk</li>
      <li>www.voltrix-installs.co.uk</li>
    </ul>
  </section>
</main>
</body>
</html>
```